Construction Company business card and Logo.

We need a business card for a Building Company.
We build and constuction manage.
A simple logo is also required. Ive attached some samples that may assist.
Logo colours: Blue,sunburnt orange,lime/green and brown/grey.
The Font for the Brenvale logo ive been using is Georgia.
Maybe the A in Brenvale can be like my logo design..?
All other font either calibri or arial, something simple.
Simple/modern and neat is what i am looking for.
My card should look organised to convey what the company is about.

Target Market(s)

Developers, architects, proffesionals in general

Industry/Entity Type

Business

Contact Information for Business Card

Brenvale Constructions Pty Ltd
ACN: 381 607 912 Lic:617382D
Derek Lomavich
Managing Director
0438 215 706
derek@brenvale.com.au
www.brenvale.com.au
Industrial.Commercial.Residential.Build Management

Requirements
Must have
• Ive attached some ideas for the logo. Its simple. If you come up with something else, please show me as im not 100% sure of what i want.
The front of the card should be white.
The back of the card should have the company name and logo with Blue background
Should not have
• the design should be simple.
No old style fonts or italics etc

```html
<!DOCTYPE html>
<html lang="en">
<head>
<meta charset="utf-8">
<title>Brenvale Constructions – Business Card</title>
<link href="https://fonts.googleapis.com/css2?family=Open+Sans:wght@400;700&display=swap" rel="stylesheet">
<style>
  :root {
    --red: #e00d0d;
    --cyan: #3ee6f7;
    --blue: #1212e6;
    --band: #6b6b6b;
    --white: #ffffff;
    --ink: #1a1a1a;
    --phone-red: #e00d0d;
    --globe-orange: #e06a10;
  }
  html, body {
    margin: 0;
    padding: 0;
    width: 1200px;
    height: 683px;
    overflow: hidden;
    background: var(--white);
  }
  .card {
    position: relative;
    width: 1200px;
    height: 683px;
    box-sizing: border-box;
    border: 10px solid var(--red);
    background: var(--white);
    font-family: "Open Sans", Arial, sans-serif;
    overflow: hidden;
  }
  .inner-frame {
    position: absolute;
    left: 18px; top: 18px; right: 18px; bottom: 18px;
    border: 11px solid var(--cyan);
  }
  .brand {
    position: absolute;
    top: 66px;
    left: 0; right: 0;
    display: flex;
    justify-content: center;
    align-items: center;
    gap: 30px;
    color: var(--blue);
    font-weight: 700;
  }
  .brand-square {
    width: 150px;
    height: 150px;
    background: var(--blue);
  }
  .brand-name {
    display: flex;
    flex-direction: column;
    line-height: 1;
  }
  .brand-name .word {
    font-size: 110px;
    letter-spacing: -1px;
  }
  .brand-name .tag {
    font-size: 26px;
    letter-spacing: 6px;
    margin-top: 8px;
    padding-left: 4px;
  }
  .services {
    position: absolute;
    left: 0; right: 0;
    top: 267px;
    height: 67px;
    background: var(--band);
    color: var(--white);
    display: flex;
    align-items: center;
    justify-content: center;
    gap: 24px;
    font-size: 43px;
    font-weight: 400;
  }
  .services .dot {
    width: 12px; height: 12px;
    border-radius: 50%;
    background: var(--white);
  }
  .person {
    position: absolute;
    left: 0; right: 0;
    top: 400px;
    text-align: center;
    color: var(--blue);
    font-weight: 700;
  }
  .person .name { font-size: 39px; line-height: 1.2; }
  .person .role { font-size: 24px; letter-spacing: 0.5px; line-height: 1.3; }
  .contacts {
    position: absolute;
    left: 0; right: 0;
    top: 542px;
    display: flex;
    justify-content: center;
    align-items: center;
    gap: 26px;
    color: var(--blue);
    font-size: 29px;
    font-weight: 700;
  }
  .contact { display: flex; align-items: center; gap: 8px; }
  .divider { width: 3px; height: 44px; background: var(--ink); }
  .icon { width: 30px; height: 30px; }
  .icon-mail { width: 40px; }
</style>
</head>
<body>
<div class="card">
  <div class="inner-frame"></div>

  <div class="brand">
    <div class="brand-square"></div>
    <div class="brand-name">
      <span class="word">Brenvale</span>
      <span class="tag">constructions (PTY) LTD</span>
    </div>
  </div>

  <div class="services">
    <span>industrial</span><span class="dot"></span>
    <span>commercial</span><span class="dot"></span>
    <span>residential</span><span class="dot"></span>
    <span>management</span>
  </div>

  <div class="person">
    <div class="name">Derek Lomavich</div>
    <div class="role">MANAGING DIRECTOR</div>
  </div>

  <div class="contacts">
    <div class="contact">
      <svg class="icon" viewBox="0 0 30 30" aria-hidden="true">
        <rect x="8" y="3" width="14" height="24" rx="2" fill="var(--phone-red)"/>
        <rect x="10" y="6" width="10" height="8" fill="#ffffff"/>
        <g fill="#ffffff">
          <rect x="10" y="16" width="2.5" height="2"/><rect x="13.75" y="16" width="2.5" height="2"/><rect x="17.5" y="16" width="2.5" height="2"/>
          <rect x="10" y="19.5" width="2.5" height="2"/><rect x="13.75" y="19.5" width="2.5" height="2"/><rect x="17.5" y="19.5" width="2.5" height="2"/>
        </g>
      </svg>
      <span>0438 215 706</span>
    </div>
    <div class="divider"></div>
    <div class="contact">
      <svg class="icon icon-mail" viewBox="0 0 30 30" aria-hidden="true">
        <rect x="2" y="7" width="26" height="17" fill="#ffffff" stroke="var(--phone-red)" stroke-width="2"/>
        <path d="M2 7 L15 18 L28 7" fill="none" stroke="var(--phone-red)" stroke-width="2"/>
      </svg>
      <span>derek@brenvale.com.au</span>
    </div>
    <div class="divider"></div>
    <div class="contact">
      <svg class="icon" viewBox="0 0 30 30" aria-hidden="true">
        <circle cx="15" cy="15" r="12" fill="#ffffff" stroke="var(--globe-orange)" stroke-width="2.2"/>
        <ellipse cx="15" cy="15" rx="5" ry="12" fill="none" stroke="var(--globe-orange)" stroke-width="1.8"/>
        <line x1="3" y1="15" x2="27" y2="15" stroke="var(--globe-orange)" stroke-width="1.8"/>
      </svg>
      <span>www.brenvale.com.au</span>
    </div>
  </div>
</div>
</body>
</html>
```